Stationary for Real Estate Investor
Holvane Estates
Stationary for Real Estate Investor - Real Estate
Creative Brief
Simple
Teodoro Vilchis
Real Estate Investor
P.O Box 417, Castro Ridge, CA 94812
teodoro@holvaneestates.example
Only use address on envelope (back flap, small print) Logo in Front Corner On letterhead only use logo (no contact info)
tvilchis27 tvilchis27
No Address on business card only on envelope.

```html
<!DOCTYPE html>
<html lang="en">
<head>
<meta charset="utf-8">
<title>Holvane Estates – Business Card</title>
<link href="https://fonts.googleapis.com/css2?family=Raleway:wght@400;500&family=Open+Sans:wght@400&display=swap" rel="stylesheet">
<style>
  :root{
    --backdrop:#dcd9d6;
    --card-dark:#2a292b;
    --panel-light:#f5f5f5;
    --panel-shade:#c6c6c8;
    --tab-grey:#b9b9bb;
    --text-light:#f2f2f2;
    --text-muted:#a9a9ab;
    --text-dark:#2a292b;
  }
  html,body{margin:0;padding:0;overflow:hidden;}
  body{width:1200px;height:802px;background:var(--backdrop);position:relative;}
  .card{position:absolute;top:252px;width:520px;height:297px;box-shadow:0 6px 18px rgba(0,0,0,.18);}
  .card--front{left:60px;}
  .card--back{left:620px;}
  .card svg{display:block;width:520px;height:297px;}
  .brand{font-family:'Raleway',sans-serif;font-weight:500;font-size:30px;letter-spacing:1px;fill:var(--text-dark);}
  .contact{font-family:'Open Sans',sans-serif;font-size:12.5px;fill:var(--text-light);letter-spacing:.4px;}
  .web{font-family:'Open Sans',sans-serif;font-size:12.5px;fill:var(--text-dark);letter-spacing:.4px;}
  .holder-name{font-family:'Raleway',sans-serif;font-weight:500;font-size:19px;letter-spacing:1.5px;fill:var(--text-light);}
  .holder-title{font-family:'Open Sans',sans-serif;font-size:11.5px;fill:var(--text-muted);letter-spacing:.5px;}
  .icon{fill:var(--text-light);}
  .icon-line{fill:none;stroke:var(--text-light);stroke-width:1.4;}
</style>
</head>
<body>

<div class="card card--front">
  <svg viewBox="0 0 520 297" xmlns="http://www.w3.org/2000/svg">
    <defs>
      <linearGradient id="panelGrad" x1="0" y1="0" x2="1" y2="0.4">
        <stop offset="0" stop-color="var(--panel-light)"/>
        <stop offset="1" stop-color="var(--panel-shade)"/>
      </linearGradient>
      <linearGradient id="bandGrad" x1="0" y1="0" x2="1" y2="0">
        <stop offset="0" stop-color="#a3a3a5"/>
        <stop offset="1" stop-color="#6f6f71"/>
      </linearGradient>
    </defs>
    <rect class="card-base" width="520" height="297" fill="var(--card-dark)"/>
    <path class="grey-band" d="M0 0H520V150H0Z" fill="url(#bandGrad)"/>
    <path class="light-panel" d="M0 24H520V138H290Q274 138 268 150Q262 162 246 162H0Z" fill="url(#panelGrad)"/>
    <path class="web-tab" d="M290 138H500Q510 138 510 148V176Q510 188 498 188H290Q278 188 278 176V150Q278 138 290 138Z" fill="var(--tab-grey)"/>
    <text class="brand" x="40" y="92">HOLVANE ESTATES</text>
    <text class="web" x="394" y="168" text-anchor="middle">www.holvaneestates.example</text>

    <g class="phone-row">
      <path class="icon" d="M28 212c2-2 4-2 5 0l3 4c1 1 0 3-1 4l-2 1c1 3 4 6 7 7l1-2c1-1 3-2 4-1l4 3c2 1 2 3 0 5-3 3-8 3-13-2s-11-12-8-19z"/>
      <text class="contact" x="60" y="218">555 014 2730</text>
      <text class="contact" x="60" y="234">555 014 2731</text>
    </g>
    <g class="email-row">
      <rect class="icon-line" x="262" y="252" width="20" height="14"/>
      <path class="icon-line" d="M262 252l10 8 10-8"/>
      <text class="contact" x="500" y="264" text-anchor="end">teodoro@holvaneestates.example</text>
    </g>
  </svg>
</div>

<div class="card card--back">
  <svg viewBox="0 0 520 297" xmlns="http://www.w3.org/2000/svg">
    <defs>
      <linearGradient id="backGrad" x1="0" y1="0" x2="1" y2="1">
        <stop offset="0" stop-color="#b4b4b6"/>
        <stop offset="1" stop-color="#7c7c7e"/>
      </linearGradient>
    </defs>
    <rect class="card-base" width="520" height="297" fill="var(--card-dark)"/>
    <path class="grey-shape" d="M0 150H150Q164 150 170 138Q176 124 192 124H330Q346 124 352 138Q358 150 372 150H520V222H372Q358 222 352 234Q346 246 330 246H192Q176 246 170 234Q164 222 150 222H0Z" fill="url(#backGrad)"/>
    <text class="holder-name" x="490" y="48" text-anchor="end">TEODORO VILCHIS</text>
    <text class="holder-title" x="490" y="68" text-anchor="end">Managing Director</text>
  </svg>
</div>

</body>
</html>
```